I'm looking for an app for customers to order through

I'm looking for an app for my customers to order products through
Ideally each customer would have a customer number with password
Their profile would come up with a preloaded products they currently order
From there they can select the product they require and volume needed for delivery
I would also like an option for them to go to a full product range if they are looking for Ideas or a product they don't currently use
Once the order is completed a copy of the order is them e-mailed to my distribution facilities and a confirmation sent to the customer by e-mail and/or SMS
Current product list is approx 1000 items
Current customers is 80 with expectations to expand to 200
On average current products ordered by each customer is is between 4-8 items
Ordering units are done by both weight and pieces/units

Target Market(s)

Food service outlets,
Restaurant , Hotels, catering companies, clubs, take away shops, cafes
Retail outlets

Number of Pages Required

1 page

Font styles to use
Sans Serif

Colors
abd037

Requirements
Must have
• Customer log in with Password 4 - 6 digit
• Customer order history
Nice to have
• Area for promotions / specials on a weekly / monthly basis

```html
<!DOCTYPE html>
<html lang="en">
<head>
<meta charset="utf-8">
<title>Oakridge Larder – Start Screen</title>
<link href="https://fonts.googleapis.com/css2?family=Raleway:wght@400;500;700&family=Source+Sans+3:wght@400&display=swap" rel="stylesheet">
<style>
  :root {
    --stage: #2e2e2e;
    --screen: #f3f5ea;
    --screen-deep: #eef1e2;
    --brand: #80a43a;
    --brand-light: #8cb142;
    --brand-circle: #e6ead8;
    --ink-dark: #222;
    --muted: #8c8c8c;
    --field-line: #d9dcd0;
    --placeholder: #b6b8b0;
    --white: #ffffff;
  }
  * { margin: 0; padding: 0; box-sizing: border-box; }
  html, body { width: 1200px; height: 1200px; overflow: hidden; }
  body {
    background: var(--stage);
    position: relative;
    font-family: "Raleway", sans-serif;
  }
  .screen {
    position: absolute;
    left: 338px; top: 113px;
    width: 522px; height: 926px;
    box-shadow: 6px 8px 14px rgba(0,0,0,0.55);
    overflow: hidden;
  }
  .screen-backdrop {
    position: absolute; inset: 0;
    background: linear-gradient(180deg, var(--screen) 0%, var(--screen-deep) 100%);
  }
  .status-bar {
    position: absolute; left: 0; top: 0; width: 100%; height: 31px;
    font-family: "Source Sans 3", sans-serif;
    font-size: 15px; color: #333;
  }
  .status-signal { position: absolute; left: 9px; top: 7px; display: flex; align-items: center; gap: 6px; }
  .status-time { position: absolute; left: 0; width: 100%; top: 6px; text-align: center; }
  .status-battery { position: absolute; right: 9px; top: 6px; display: flex; align-items: center; gap: 5px; }
  .brand-plate {
    position: absolute; left: 130px; top: 122px; width: 266px; height: 107px;
    background: var(--brand-light);
    box-shadow: 0 2px 3px rgba(0,0,0,0.2);
    display: flex; align-items: center; justify-content: center; gap: 12px;
  }
  .brand-dot { width: 38px; height: 38px; border-radius: 50%; background: var(--brand-circle); }
  .brand-name {
    font-weight: 700; font-size: 21px; line-height: 1.05; color: var(--ink-dark);
    letter-spacing: 0.5px;
  }
  .welcome {
    position: absolute; left: 0; width: 100%; top: 274px;
    text-align: center; font-size: 34px; font-weight: 400; color: var(--brand);
  }
  .welcome strong { font-weight: 700; }
  .tagline {
    position: absolute; left: 0; width: 100%; top: 326px;
    text-align: center; font-size: 20px; color: var(--muted);
  }
  .field {
    position: absolute; left: 59px; width: 406px; height: 54px;
    border: 1px solid var(--field-line);
    display: flex; align-items: center;
  }
  .field-phone { top: 415px; }
  .field-password { top: 480px; }
  .field-icon { width: 46px; display: flex; justify-content: center; }
  .field-divider { width: 1px; height: 26px; background: var(--field-line); }
  .field-label { padding-left: 14px; font-size: 20px; color: var(--placeholder); }
  .go-button {
    position: absolute; left: 59px; top: 576px; width: 406px; height: 54px;
    background: var(--brand); color: var(--white);
    font-size: 19px; font-weight: 500;
    display: flex; align-items: center; justify-content: center;
  }
  .forgot-link {
    position: absolute; left: 0; width: 100%; top: 661px;
    text-align: center; font-size: 18px; color: var(--muted);
  }
  .version {
    position: absolute; left: 0; width: 100%; top: 896px;
    text-align: center; font-family: "Source Sans 3", sans-serif;
    font-size: 14px; color: var(--muted);
  }
  .screen-caption {
    position: absolute; left: 0; width: 100%; top: 1094px;
    text-align: center; font-family: "Source Sans 3", sans-serif;
    font-size: 33px; color: var(--white);
  }
</style>
</head>
<body>
  <main class="screen">
    <div class="screen-backdrop" role="img" aria-label="Faint pale-green pattern of hand-drawn clothing and accessory doodles"></div>

    <div class="status-bar">
      <div class="status-signal">
        <svg width="50" height="10" viewBox="0 0 50 10">
          <circle cx="5" cy="5" r="4" fill="#333"/><circle cx="14" cy="5" r="4" fill="#333"/>
          <circle cx="23" cy="5" r="4" fill="#333"/><circle cx="32" cy="5" r="3.5" fill="none" stroke="#333"/>
          <circle cx="41" cy="5" r="3.5" fill="none" stroke="#333"/>
        </svg>
        <span>Tellora</span>
        <svg width="18" height="13" viewBox="0 0 18 13" style="margin-left:12px">
          <path d="M1 4.5a11 11 0 0 1 16 0" fill="none" stroke="#333" stroke-width="2"/>
          <path d="M4 7.5a6.5 6.5 0 0 1 10 0" fill="none" stroke="#333" stroke-width="2"/>
          <circle cx="9" cy="11" r="1.8" fill="#333"/>
        </svg>
      </div>
      <div class="status-time">4:21 PM</div>
      <div class="status-battery">
        <span>100%</span>
        <svg width="32" height="13" viewBox="0 0 32 13">
          <rect x="0.5" y="0.5" width="28" height="12" rx="1.5" fill="none" stroke="#333"/>
          <rect x="2" y="2" width="25" height="9" fill="#555"/>
          <rect x="29.5" y="4" width="2" height="5" fill="#333"/>
        </svg>
      </div>
    </div>

    <div class="brand-plate">
      <span class="brand-dot"></span>
      <span class="brand-name">OAKRIDGE<br>LARDER</span>
    </div>

    <h1 class="welcome">Welcome to <strong>O.L.</strong></h1>
    <p class="tagline">Lorem Ipsum is simply dummy text</p>

    <div class="field field-phone">
      <span class="field-icon">
        <svg width="22" height="22" viewBox="0 0 24 24">
          <path d="M6.6 10.8a15.1 15.1 0 0 0 6.6 6.6l2.2-2.2a1 1 0 0 1 1-.25 11.4 11.4 0 0 0 3.6.57 1 1 0 0 1 1 1V20a1 1 0 0 1-1 1A17 17 0 0 1 3 4a1 1 0 0 1 1-1h3.5a1 1 0 0 1 1 1c0 1.25.2 2.450.57 3.57a1 1 0 0 1-.25 1z" fill="var(--brand)"/>
        </svg>
      </span>
      <span class="field-divider"></span>
      <span class="field-label">Phone Number</span>
    </div>

    <div class="field field-password">
      <span class="field-icon">
        <svg width="18" height="24" viewBox="0 0 18 24">
          <path d="M4 10V7a5 5 0 0 1 10 0v3" fill="none" stroke="var(--brand)" stroke-width="2.2"/>
          <rect x="1" y="10" width="16" height="13" fill="var(--brand)"/>
        </svg>
      </span>
      <span class="field-divider"></span>
      <span class="field-label">Password</span>
    </div>

    <div class="go-button">GO</div>
    <p class="forgot-link">Forget password?</p>
    <p class="version">v 1.0.1</p>
  </main>

  <p class="screen-caption">Start Screen</p>
</body>
</html>
```